Business card / stationery design
Pemberton Hale Warrick
Project: Business card / stationery design
Business card / stationery design - Engineering
Creative Brief
Use specific fonts
Gill Sans MT, Calibri, Corbel, Lucida Sans UC or similar
Professional
Derek R. Pemberton, P.E., LEED A.P., CPMP
Principal
4738 E. Harrowgate Ave., Suite C-212B, Springfield, Missouri 65809
dpemberton@pembertonhalewarrick.example
www.pembertonhalewarrick.example
We would like to use only the logo from the attached file. We like the current color arrangement, but would be interested in seeing it in other colors. Also the slightly gray color behind the logo should just be white or whatever the background color is. A couple of examples are attached. The main text adjacent to the logo should read: Pemberton Hale Warrick. Secondary text will be similar to: Engineering & Energy Services.
We are interested in your ideas.

```html
<!DOCTYPE html>
<html lang="en">
<head>
<meta charset="utf-8">
<title>Pemberton Hale Warrick — Stationery</title>
<link href="https://fonts.googleapis.com/css2?family=Lato:wght@400;700&display=swap" rel="stylesheet">
<style>
:root{
  --bg:#e9e6e1;
  --paper:#ffffff;
  --green:#7ab648;
  --green-dark:#4f8f2c;
  --blue:#1c63ad;
  --blue-dark:#0d3f7a;
  --ink:#3b3f45;
  --muted:#8a9096;
  --rule:#c9ccd0;
  --faint:#eef3ea;
}
*{box-sizing:border-box;margin:0;padding:0}
html,body{width:1200px;height:562px;overflow:hidden;background:var(--bg);font-family:"Lato",sans-serif;color:var(--ink)}
.stage{position:relative;width:1200px;height:562px}
.sheet{position:absolute;background:var(--paper);box-shadow:0 2px 6px rgba(0,0,0,.18);overflow:hidden}
.corner{position:absolute;display:block}
.corner-tl{top:0;left:0}
.corner-br{bottom:0;right:0}
.brand{position:absolute;display:flex;align-items:center;gap:5px}
.brand-mark{width:14px;height:14px;background:var(--blue)}
.brand-name{font-size:6px;font-weight:700;letter-spacing:.4px;text-transform:uppercase;color:var(--blue-dark)}
.watermark{position:absolute;background:var(--faint);opacity:.9}
.footer{position:absolute;font-size:4.6px;line-height:1.5;color:var(--muted)}

/* letterhead */
.letterhead{left:48px;top:89px;width:348px;height:420px}
.letterhead .brand{left:30px;top:22px}
.letterhead .watermark{left:112px;top:168px;width:120px;height:120px}
.letterhead .footer{left:30px;bottom:18px}

/* fax */
.fax{left:425px;top:89px;width:343px;height:420px}
.fax .brand{left:30px;top:22px}
.fax-title{position:absolute;left:30px;top:78px;font-size:17px;font-weight:400;letter-spacing:1px}
.fax-fields{position:absolute;left:30px;top:110px;width:290px;display:grid;grid-template-columns:1fr 1fr;column-gap:14px}
.fax-field{font-size:5px;color:var(--muted);border-bottom:1px solid var(--rule);padding:4px 0 2px}
.fax-checks{position:absolute;left:30px;top:208px;display:flex;gap:12px;font-size:5px;color:var(--muted)}
.fax-checks span::before{content:"";display:inline-block;width:5px;height:5px;border:1px solid var(--muted);margin-right:3px;vertical-align:-1px}
.fax .footer{left:30px;bottom:18px}

/* cards */
.card-front{left:804px;top:89px;width:122px;height:70px}
.card-front .brand{left:10px;top:9px}
.card-front .brand-mark{width:10px;height:10px}
.card-front .brand-name{font-size:4px}
.card-contact{position:absolute;right:10px;top:8px;text-align:right;font-size:3.6px;line-height:1.5;color:var(--muted)}
.card-contact strong{display:block;color:var(--ink);font-size:4.4px}
.card-back{left:912px;top:204px;width:144px;height:74px;background:linear-gradient(135deg,var(--blue) 0%,var(--blue-dark) 100%)}
.card-back .brand{left:34px;top:31px}
.card-back .brand-mark{width:12px;height:12px;background:#fff}
.card-back .brand-name{font-size:4.6px;color:#fff}

/* envelope */
.envelope{left:828px;top:300px;width:334px;height:209px}
.env-band{position:absolute;left:0;top:0;width:100%;height:30px;background:linear-gradient(180deg,var(--blue) 0%,var(--blue-dark) 100%);color:#fff;font-size:6px;letter-spacing:.6px;text-align:center;line-height:30px}
.envelope .brand{left:44px;top:48px}
.envelope .footer{left:44px;top:70px}
.envelope .watermark{right:26px;bottom:26px;width:74px;height:74px}
</style>
</head>
<body>
<main class="stage">

  <section class="sheet letterhead" aria-label="Letterhead">
    <svg class="corner corner-tl" width="70" height="56" viewBox="0 0 70 56" aria-hidden="true">
      <polygon points="0,0 70,0 62,10 10,10 10,48 0,56" fill="var(--green)"/>
    </svg>
    <div class="brand"><span class="brand-mark"></span><span class="brand-name">Pemberton Hale Warrick</span></div>
    <div class="watermark" role="img" aria-label="Faint brand square"></div>
    <p class="footer">4738 E. Harrowgate Ave., Suite C-212B, Springfield, Missouri 65809 &nbsp;|&nbsp; 417-555-0148 &nbsp;|&nbsp; www.pembertonhalewarrick.example</p>
    <svg class="corner corner-br" width="70" height="56" viewBox="0 0 70 56" aria-hidden="true">
      <polygon points="70,56 0,56 8,46 60,46 60,8 70,0" fill="var(--blue)"/>
    </svg>
  </section>

  <section class="sheet fax" aria-label="Fax cover sheet">
    <svg class="corner corner-tl" width="70" height="56" viewBox="0 0 70 56" aria-hidden="true">
      <polygon points="0,0 70,0 62,10 10,10 10,48 0,56" fill="var(--green)"/>
    </svg>
    <div class="brand"><span class="brand-mark"></span><span class="brand-name">Pemberton Hale Warrick</span></div>
    <h1 class="fax-title">FAX</h1>
    <div class="fax-fields">
      <div class="fax-field">To:</div><div class="fax-field">From:</div>
      <div class="fax-field">Fax:</div><div class="fax-field">Pages:</div>
      <div class="fax-field">Phone:</div><div class="fax-field">Date:</div>
      <div class="fax-field">Re:</div><div class="fax-field">CC:</div>
    </div>
    <div class="fax-checks">
      <span>Urgent</span><span>For Review</span><span>Please Comment</span><span>Please Reply</span><span>Please Recycle</span>
    </div>
    <p class="footer">4738 E. Harrowgate Ave., Suite C-212B, Springfield, Missouri 65809<br>Phone 417-555-0148 &nbsp;|&nbsp; Fax 417-555-0149</p>
    <svg class="corner corner-br" width="70" height="56" viewBox="0 0 70 56" aria-hidden="true">
      <polygon points="70,56 0,56 8,46 60,46 60,8 70,0" fill="var(--blue)"/>
    </svg>
  </section>

  <section class="sheet card-front" aria-label="Business card front">
    <svg class="corner corner-tl" width="30" height="24" viewBox="0 0 30 24" aria-hidden="true">
      <polygon points="0,0 30,0 26,4 4,4 4,20 0,24" fill="var(--green)"/>
    </svg>
    <div class="brand"><span class="brand-mark"></span><span class="brand-name">Pemberton Hale Warrick</span></div>
    <p class="card-contact"><strong>Derek R. Pemberton</strong>Principal<br>417-555-0148<br>dpemberton@pembertonhalewarrick.example</p>
    <svg class="corner corner-br" width="30" height="24" viewBox="0 0 30 24" aria-hidden="true">
      <polygon points="30,24 0,24 4,20 26,20 26,4 30,0" fill="var(--blue)"/>
    </svg>
  </section>

  <section class="sheet card-back" aria-label="Business card back">
    <div class="brand"><span class="brand-mark"></span><span class="brand-name">Pemberton Hale Warrick</span></div>
  </section>

  <section class="sheet envelope" aria-label="Envelope">
    <div class="env-band">www.pembertonhalewarrick.example</div>
    <svg class="corner corner-tl" width="60" height="70" viewBox="0 0 60 70" aria-hidden="true" style="top:30px">
      <polygon points="0,0 60,0 52,8 8,8 8,62 0,70" fill="var(--green)"/>
    </svg>
    <div class="brand"><span class="brand-mark"></span><span class="brand-name">Pemberton Hale Warrick</span></div>
    <p class="footer">4738 E. Harrowgate Ave., Suite C-212B<br>Springfield, Missouri 65809</p>
    <div class="watermark" role="img" aria-label="Faint brand square"></div>
    <svg class="corner corner-br" width="60" height="50" viewBox="0 0 60 50" aria-hidden="true">
      <polygon points="60,50 0,50 8,42 52,42 52,8 60,0" fill="var(--blue)"/>
    </svg>
  </section>

</main>
</body>
</html>
```